Fabric Store Business card

Need a business card portraying store logo and up and coming business of quilt fabrics, apparel fabrics, notions and buttons. Our business name is Gilded Thimble and Such. Am attaching logo. The design should communicate a growing business and warm atmosphere. Would like address and store hours and contact info displayed on card. Mon - Fri 9:30 to 5:00, Saturday 9:30 to 1:00. Address 287 W Alder Ave, Newton, KS 67392 email: gildedthimbleandsuch@mailbrook.net. Phone and fax 316-555-2846. After hours contact # 620-555-3914 Also like vintage sewing machines and dress forms if it works to incorporate fine, if not thats ok too.

```html
<!DOCTYPE html>
<html lang="en">
<head>
<meta charset="utf-8">
<title>Gilded Thimble and Such — Business Card</title>
<link href="https://fonts.googleapis.com/css2?family=Questrial&display=swap" rel="stylesheet">
<style>
  :root {
    --bg: #e9e6e2;
    --paper: #f7f7f6;
    --red: #b8202f;
    --red-deep: #9c1a27;
    --red-light: #c9394a;
    --ink: #3c3c3c;
    --white: #ffffff;
    --stitch: #f2a3ab;
  }
  * { box-sizing: border-box; margin: 0; padding: 0; }
  html, body { width: 1200px; height: 900px; overflow: hidden; }
  body {
    background: var(--bg);
    font-family: "Questrial", "Century Gothic", sans-serif;
    position: relative;
  }
  .card {
    position: absolute;
    left: 320px;
    width: 560px;
    height: 320px;
    overflow: hidden;
    box-shadow: 0 6px 18px rgba(0,0,0,0.15);
  }
  .card--front { top: 100px; background: var(--paper); }
  .card--back { top: 480px; background: var(--red); }

  .brand {
    position: absolute;
    display: flex;
    align-items: center;
    gap: 12px;
  }
  .brand__dot { width: 30px; height: 30px; border-radius: 50%; flex: none; }
  .brand__name { font-size: 22px; letter-spacing: 0.5px; }
  .card--front .brand { left: 36px; top: 36px; }
  .card--front .brand__dot { background: var(--red); }
  .card--front .brand__name { color: var(--red); }

  .contact { position: absolute; left: 40px; top: 140px; color: var(--ink); font-size: 13px; letter-spacing: 0.6px; }
  .contact__label { font-weight: 700; font-size: 14px; letter-spacing: 1px; margin-bottom: 4px; }
  .contact__address { margin-bottom: 12px; }
  .contact__row { display: flex; align-items: center; gap: 10px; margin-bottom: 9px; }
  .contact__row svg { width: 13px; height: 13px; flex: none; }

  .swoosh { position: absolute; inset: 0; width: 100%; height: 100%; }
  .after-hours {
    fill: var(--white);
    font-family: "Questrial", "Century Gothic", sans-serif;
    font-size: 10.5px;
    letter-spacing: 0.6px;
  }

  .card--back .brand { left: 36px; top: 30px; }
  .card--back .brand__dot { background: var(--white); }
  .card--back .brand__name { color: var(--white); }
  .hours-band {
    position: absolute;
    left: 0; right: 0;
    top: 96px; height: 176px;
    background: var(--red-deep);
    border-top: 2px dashed var(--stitch);
    border-bottom: 2px dashed var(--stitch);
    display: flex;
    align-items: center;
    justify-content: space-evenly;
    color: var(--white);
    text-transform: uppercase;
    text-align: center;
  }
  .hours__day { font-size: 30px; letter-spacing: 2px; }
  .hours__time { font-size: 24px; letter-spacing: 1.5px; margin-top: 6px; }
  .hours__divider { width: 0; height: 100px; border-left: 2px dashed var(--stitch); }
</style>
</head>
<body>
  <section class="card card--front" aria-label="Business card front">
    <svg class="swoosh" viewBox="0 0 560 320">
      <defs>
        <path id="after-hours-line" d="M340 314 Q510 296 554 200"/>
      </defs>
      <path d="M250 320 Q470 300 560 110 L560 320 Z" fill="var(--red-light)"/>
      <path d="M285 320 Q480 300 560 140 L560 320 Z" fill="var(--red-deep)"/>
      <text class="after-hours">
        <textPath href="#after-hours-line" startOffset="8">After hours contact # 620-555-3914</textPath>
      </text>
    </svg>
    <div class="brand">
      <span class="brand__dot"></span>
      <span class="brand__name">Gilded Thimble and Such</span>
    </div>
    <div class="contact">
      <p class="contact__label">Address</p>
      <p class="contact__address">287 W Alder Ave, Newton, KS 67392</p>
      <p class="contact__row">
        <svg viewBox="0 0 16 16"><rect x="1" y="3" width="14" height="10" fill="none" stroke="var(--red)" stroke-width="1.6"/><path d="M1 3 L8 9 L15 3" fill="none" stroke="var(--red)" stroke-width="1.6"/></svg>
        gildedthimbleandsuch@mailbrook.net
      </p>
      <p class="contact__row">
        <svg viewBox="0 0 16 16"><path d="M2 6 Q8 1 14 6 L12 8 L10 6.5 L6 6.5 L4 8 Z M4 9 H12 L13 14 H3 Z" fill="var(--red)"/></svg>
        316-555-2846
      </p>
      <p class="contact__row">
        <svg viewBox="0 0 16 16"><path d="M2 6 Q8 1 14 6 L12 8 L10 6.5 L6 6.5 L4 8 Z M4 9 H12 L13 14 H3 Z" fill="var(--red)"/></svg>
        316-555-2846
      </p>
    </div>
  </section>

  <section class="card card--back" aria-label="Business card back">
    <div class="brand">
      <span class="brand__dot"></span>
      <span class="brand__name">Gilded Thimble and Such</span>
    </div>
    <div class="hours-band">
      <div class="hours">
        <p class="hours__day">Mon - Fri</p>
        <p class="hours__time">9:30 to 5:00</p>
      </div>
      <span class="hours__divider"></span>
      <div class="hours">
        <p class="hours__day">Saturday</p>
        <p class="hours__time">9:30 to 1:00</p>
      </div>
    </div>
  </section>
</body>
</html>
```